Boho Flower and Curiosities Shop Needs a Non-tradtional Calendar of Events

Hi! I own a cute flower shop called Meadowlark Petals. I have lots of things going on at the shop and I'd love a calendar of events poster to put around town. I already have dates and times and descriptions. I have a very boho aesthetic, creative, whimsical and different. I'd like this calendar of events to be not cookie cutter. Something interesting with images and interesting font that matches my logo. Not a super busy design.

My events can be found here: https://www.meadowlarkpetals.example/calendar-of-events

I want to be able to easily edit the poster so I can use it in the future.

Target Market(s)

Locals who want an alternative something to do.

Industry/Entity Type

Shop

Colors

Designer to choose colors to be used in the design.

Requirements
Must have
• must have the same kind of vibe that my logo and especially the mural on my building has (I submitted an image of the building). Unique, not cheesy.
• Must be editable so I can use it in the future.
Nice to have
• I want it to have a call to action such as visit my website "www.meadowlarkpetals.example". Also I like the idea of calling it Shop Happenings instead of Events Calendar.
• It might be cool to have the events coming off of a dream catcher like (but not exactly in fact I think it can be more whimsical and perhaps my logo in the middle of the catcher) the one attached.
Should not have
• If you do include flowers - no roses or daisies! Please.

```html
<!DOCTYPE html>
<html lang="en">
<head>
<meta charset="utf-8">
<title>Shop Happenings – Meadowlark Petals</title>
<link rel="stylesheet" href="https://fonts.googleapis.com/css2?family=Kaushan+Script&family=Open+Sans:wght@400&display=swap">
<style>
  :root {
    --page-bg: #e4e5e7;
    --ink: #141414;
    --ink-soft: #333333;
    --ring: #e4834a;
    --band-green: #7dc242;
    --band-orange: #e3824a;
    --wash-blue: #d9e8f7;
    --wash-green: #dcecc8;
    --wash-pink: #fbe9ee;
    --paper: #f8fafc;
    --cta-pink: #e3aeb7;
    --cta-orange: #e3814a;
    --cta-lime: #e1efc0;
    --petal: #f9cdb0;
    --leaf: #9cc48a;
  }
  * { margin: 0; padding: 0; box-sizing: border-box; }
  html, body { width: 1163px; height: 1200px; overflow: hidden; background: var(--page-bg); }
  .poster {
    position: absolute; left: 171px; top: 20px;
    width: 800px; height: 1132px;
    transform: scale(1.025); transform-origin: 0 0;
    overflow: hidden;
    font-family: "Open Sans", Arial, sans-serif; color: var(--ink);
    background:
      radial-gradient(ellipse 420px 380px at 80px 300px, var(--wash-blue), transparent 70%),
      radial-gradient(ellipse 460px 420px at 120px 750px, var(--wash-green), transparent 70%),
      radial-gradient(ellipse 420px 380px at 680px 260px, var(--wash-pink), transparent 70%),
      radial-gradient(ellipse 360px 300px at 620px 760px, #e2edf8, transparent 70%),
      var(--paper);
  }
  .header-stripe { position: absolute; left: 0; top: 22px; width: 440px; height: 8px;
    background: linear-gradient(90deg, var(--band-orange) 70%, rgba(227,130,74,0)); }
  .header-band { position: absolute; left: 0; top: 30px; width: 540px; height: 88px;
    background: linear-gradient(90deg, var(--band-green) 0%, #b9db95 50%, rgba(220,236,200,0) 100%); }
  .title { position: absolute; left: 46px; top: 42px; font-family: "Kaushan Script", cursive;
    font-size: 58px; font-weight: 400; line-height: 1; color: var(--ink); letter-spacing: -1px; white-space: nowrap; }
  .floral { position: absolute; }
  .floral-top { right: -40px; top: -30px; width: 420px; height: 360px; border-radius: 50%;
    background: radial-gradient(circle at 62% 30%, var(--petal) 0 18%, transparent 32%),
                radial-gradient(ellipse at 40% 40%, rgba(156,196,138,.75), transparent 60%); }
  .floral-bottom { left: -40px; bottom: -40px; width: 470px; height: 360px; border-radius: 50%;
    background: radial-gradient(circle at 30% 70%, var(--petal) 0 18%, transparent 32%),
                radial-gradient(ellipse at 50% 60%, rgba(156,196,138,.7), transparent 62%); }
  .cta-shapes { position: absolute; left: 0; top: 0; width: 800px; height: 1132px; }
  .cta { position: absolute; left: 462px; top: 1008px; width: 320px; }
  .cta-heading { font-family: "Kaushan Script", cursive; font-size: 38px; font-weight: 400; line-height: 1; color: var(--ink); white-space: nowrap; }
  .cta-url { font-size: 19px; margin-top: 10px; color: var(--ink); white-space: nowrap; }
  .brand { position: absolute; left: 270px; top: 408px; width: 250px; height: 250px; border-radius: 50%;
    display: flex; align-items: center; justify-content: center; text-align: center;
    background: radial-gradient(circle, rgba(255,255,255,0) 48%, rgba(156,196,138,.55) 55%, rgba(249,205,176,.5) 68%, rgba(255,255,255,0) 76%); }
  .brand-name { font-size: 30px; line-height: 1.15; color: var(--ink); }
  .event { position: absolute; width: 210px; margin-left: -105px; text-align: center; }
  .event-photo { display: block; width: 94px; height: 94px; margin: 0 auto; border-radius: 50%;
    border: 2px solid var(--ring); padding: 4px; background-clip: content-box; }
  .event-title { font-size: 16px; font-weight: 400; line-height: 22px; margin-top: 8px; color: var(--ink); }
  .event-when, .event-where { font-size: 11px; line-height: 16px; color: var(--ink-soft); margin-top: 9px; }
  .photo-oyster { background-color: #8a8272; background-image: radial-gradient(circle at 40% 40%, #b5ab96, #5f584c); }
  .photo-terrarium { background-image: radial-gradient(circle at 45% 55%, #6e7a5a, #2f3226); }
  .photo-crown { background-image: radial-gradient(circle at 50% 40%, #d9b9a4, #9b2c30); }
  .photo-bouquet { background-image: radial-gradient(circle at 50% 50%, #f1c9d6, #a3234f 75%); }
  .photo-dinner { background-image: radial-gradient(circle at 50% 55%, #f4f4f0, #b6c3b4); }
  .photo-fairy { background-image: radial-gradient(circle at 50% 60%, #4e7a2c, #2a2f26); }
  .photo-mandrake { background-image: radial-gradient(circle at 50% 45%, #5d7c4b, #efe9e0 80%); }
</style>
</head>
<body>
<main class="poster">
  <div class="floral floral-top" role="img" aria-label="Watercolour peach blossoms and succulent leaves"></div>
  <div class="floral floral-bottom" role="img" aria-label="Watercolour peach blossom, succulents and grasses"></div>

  <div class="header-stripe"></div>
  <div class="header-band"></div>
  <h1 class="title">Shop Happenings</h1>

  <div class="brand">
    <span class="brand-name">Meadowlark<br>Petals</span>
  </div>

  <section class="event" style="left:166px; top:224px;">
    <span class="event-photo photo-oyster" role="img" aria-label="Photo of fresh oysters"></span>
    <h2 class="event-title">Tidewater Oyster<br>Farms...Roast!</h2>
    <p class="event-when">Sun, Jan 21, 2018 at<br>2:00pm - 5:00pm EST</p>
    <p class="event-where">Meadowlark Petals, 118<br>Linden Row, Harbor Point,<br>SC 29999, USA</p>
  </section>

  <section class="event" style="left:396px; top:153px;">
    <span class="event-photo photo-terrarium" role="img" aria-label="Photo of a terrarium being planted"></span>
    <h2 class="event-title">Terrariums &amp; Tapas</h2>
    <p class="event-when">Wed, Jan 31, 2018 at<br>5:30pm - 7:00pm EST</p>
    <p class="event-where">Meadowlark Petals, 118<br>Linden Row, Harbor Point,<br>SC 29999, USA</p>
  </section>

  <section class="event" style="left:618px; top:224px;">
    <span class="event-photo photo-crown" role="img" aria-label="Photo of two children wearing flower crowns"></span>
    <h2 class="event-title">Mother Daughter<br>Flower Crown Making</h2>
    <p class="event-when">Sat, Feb 10, 2018 at<br>10:30am - 12:00pm EST</p>
    <p class="event-where">Meadowlark Petals, 118<br>Linden Row, Harbor Point,<br>SC 29999, USA</p>
  </section>

  <section class="event" style="left:146px; top:512px;">
    <span class="event-photo photo-bouquet" role="img" aria-label="Photo of a colourful flower arrangement"></span>
    <h2 class="event-title">Galentine's Day Flower<br>Arranging</h2>
    <p class="event-when">Tue, Feb 13, 2018 at<br>5:30pm - 7:00pm EST</p>
    <p class="event-where">Meadowlark Petals, 118<br>Linden Row, Harbor Point,<br>SC 29999, USA</p>
  </section>

  <section class="event" style="left:657px; top:512px;">
    <span class="event-photo photo-dinner" role="img" aria-label="Photo of a set dinner table"></span>
    <h2 class="event-title">Valentine's Pop-up<br>Dinner</h2>
    <p class="event-when">Wed, Feb 14, 2018 at<br>6:00pm - 8:00pm EST</p>
    <p class="event-where">Meadowlark Petals, 118<br>Linden Row, Harbor Point,<br>SC 29999, USA</p>
  </section>

  <section class="event" style="left:301px; top:700px;">
    <span class="event-photo photo-fairy" role="img" aria-label="Photo of a mossy fairy garden terrarium"></span>
    <h2 class="event-title">Fairy Garden<br>Terrariums</h2>
    <p class="event-when">Sat, Mar 3, 2018 at<br>10:30am - 12:00pm EST</p>
    <p class="event-where">Meadowlark Petals, 118<br>Linden Row, Harbor Point,<br>SC 29999, USA</p>
  </section>

  <section class="event" style="left:493px; top:700px;">
    <span class="event-photo photo-mandrake" role="img" aria-label="Botanical print of a mandrake plant"></span>
    <h2 class="event-title">Mandrake Print<br>Making</h2>
    <p class="event-when">Wed, Mar 14, 2018 at<br>5:30pm - 7:00pm EDT</p>
    <p class="event-where">Meadowlark Petals, 118<br>Linden Row, Harbor Point,<br>SC 29999, USA</p>
  </section>

  <svg class="cta-shapes" viewBox="0 0 800 1132" aria-hidden="true">
    <polygon points="585,962 693,862 770,925 690,968" fill="var(--cta-lime)"/>
    <polygon points="650,955 800,907 800,993 700,970" fill="var(--cta-orange)"/>
    <polygon points="413,1012 612,946 800,993 800,1132 432,1132" fill="var(--cta-pink)"/>
  </svg>
  <div class="cta">
    <p class="cta-heading">Visit my website</p>
    <p class="cta-url">www.meadowlarkpetals.example</p>
  </div>
</main>
</body>
</html>
```